Take away menu for italian restaurant

We need a brochure for take away. I was thinking about a A4 page with take away for partys on one page and the other with take away for every day. The page with the party menu I want a big very nice food picture. The other site with meals for every day sound be as simple as possible so people do not get too confused over the many different options. so it is very important that it is easy to look at the every day menu. i hope it is possible for you to just use google translate so you know what is what. if not I can try to translate it. but we only need it in danish.

```html
<!DOCTYPE html>
<html lang="da">
<head>
<meta charset="utf-8">
<title>Trattoria Verde – take away brochure</title>
<link href="https://fonts.googleapis.com/css2?family=Didact+Gothic&display=swap" rel="stylesheet">
<style>
  :root {
    --paper: #ffffff;
    --canvas: #ffffff;
    --ink: #2a2a2a;
    --heading-grey: #8a8a8a;
    --footer-grey: #7d7d7d;
    --page-border: #9a9a9a;
    --flag-green: #4aa04a;
    --flag-red: #d8262e;
    --accent-red: #d8262e;
    --gold-light: #ffe34d;
    --gold-dark: #f2b707;
    --mint: #cfe9c8;
    --blush: #f2c7cb;
  }
  * { box-sizing: border-box; margin: 0; padding: 0; }
  html, body { width: 1200px; height: 833px; overflow: hidden; background: var(--canvas); }
  body { position: relative; font-family: "Didact Gothic", "Century Gothic", sans-serif; color: var(--ink); }

  .page {
    position: absolute; top: 73px; width: 500px; height: 703px;
    background: var(--paper); border: 1px solid var(--page-border); overflow: hidden;
  }
  .page--party { left: 69px; }
  .page--everyday { left: 636px; }

  .flag-corner { position: absolute; left: 0; top: 0; width: 84px; height: 84px; }

  /* Party page */
  .party-title {
    position: absolute; left: 108px; top: 24px; white-space: nowrap;
    font-size: 21px; line-height: 24px; letter-spacing: 0.5px; color: var(--heading-grey); font-weight: 400;
  }
  .party-intro { position: absolute; left: 108px; top: 80px; width: 225px; font-size: 9px; line-height: 11.5px; }

  .price-badge {
    position: absolute; left: 352px; top: 22px; width: 116px; height: 116px; border-radius: 50%;
    background: radial-gradient(circle at 40% 35%, var(--gold-light), var(--gold-dark));
    color: var(--accent-red); text-align: center; transform: rotate(-12deg);
    display: flex; flex-direction: column; justify-content: center; align-items: center;
  }
  .price-badge__label { font-size: 15px; line-height: 16px; }
  .price-badge__amount { font-size: 26px; line-height: 26px; }
  .price-badge__unit { font-size: 17px; line-height: 18px; }
  .price-badge__note { font-size: 7px; line-height: 9px; margin-top: 2px; color: var(--ink); }

  .hero-photo { position: absolute; left: 0; top: 132px; width: 500px; height: 412px; }

  .course-list { position: absolute; top: 560px; font-size: 9px; line-height: 11.5px; list-style: none; }
  .course-list li { position: relative; padding-left: 10px; margin-bottom: 3px; }
  .course-list li::before { content: "•"; position: absolute; left: 0; }
  .course-list--first { left: 13px; width: 235px; }
  .course-list--second { left: 262px; width: 215px; }

  .bread-note { position: absolute; left: 262px; top: 620px; width: 210px; font-size: 11px; line-height: 14px; }
  .closing-line { position: absolute; left: 162px; top: 666px; font-size: 25px; color: var(--accent-red); }
  .corner-mark { position: absolute; left: 481px; top: 648px; width: 9px; height: 9px; border: 1px solid var(--accent-red); }

  /* Everyday page */
  .everyday-title {
    position: absolute; left: 0; top: 28px; width: 100%; text-align: center; white-space: nowrap;
    font-size: 21px; line-height: 25px; letter-spacing: 1.5px; color: var(--heading-grey); font-weight: 400;
  }
  .everyday-intro { position: absolute; left: 26px; top: 106px; width: 448px; font-size: 9.5px; line-height: 12px; text-align: center; }

  .menu-column { position: absolute; top: 212px; height: 371px; padding: 14px 10px; font-size: 8.6px; line-height: 11px; }
  .menu-column p { margin-bottom: 11px; }
  .menu-column--family { left: 0; width: 126px; background: linear-gradient(to bottom, var(--mint), #f3faf1); }
  .menu-column--pairs { left: 179px; width: 142px; padding-left: 0; }
  .menu-column--single { left: 335px; width: 165px; background: linear-gradient(to bottom, var(--blush), #fbeeef); }
  .menu-column__intro { font-weight: 700; }

  .order-footer {
    position: absolute; left: 0; top: 650px; width: 100%; text-align: center;
    font-size: 9.5px; line-height: 13px; letter-spacing: 0.6px; color: var(--footer-grey); text-transform: uppercase;
  }
</style>
</head>
<body>

<section class="page page--party">
  <svg class="flag-corner" viewBox="0 0 84 84" aria-hidden="true">
    <polygon points="0,40 40,0 56,0 0,56" fill="var(--flag-green)"/>
    <polygon points="0,56 56,0 66,0 0,66" fill="#ffffff"/>
    <polygon points="0,66 66,0 84,0 0,84" fill="var(--flag-red)"/>
  </svg>

  <h1 class="party-title">5-RETTERS ITALIENSK<br>FEST MENU</h1>
  <p class="party-intro">Til en dag hvor du ikke orker at kokkerere til dine gæster, men ønsker at give dem en fantastisk madoplevelse. Du sørger selv for hyggen.</p>

  <div class="price-badge">
    <span class="price-badge__label">Pris</span>
    <span class="price-badge__amount">295 kr.</span>
    <span class="price-badge__unit">per kuvert</span>
    <span class="price-badge__note">(ved min. 10 personer)</span>
  </div>

  <svg class="hero-photo" viewBox="0 0 500 412" role="img" aria-label="Foto af tigerrejer på risotto med laks og purløg">
    <defs>
      <linearGradient id="food-tones" x1="0" y1="0" x2="1" y2="1">
        <stop offset="0" stop-color="#ecebe6"/>
        <stop offset="0.45" stop-color="#e8b48f"/>
        <stop offset="0.75" stop-color="#d9c48a"/>
        <stop offset="1" stop-color="#b98a5a"/>
      </linearGradient>
    </defs>
    <path d="M0,60 C140,10 330,-10 500,20 L500,412 L0,412 Z" fill="url(#food-tones)"/>
    <path d="M0,330 C160,400 360,410 500,360 L500,412 L0,412 Z" fill="var(--paper)"/>
  </svg>

  <ul class="course-list course-list--first">
    <li>Dampet laks på en bund af spæde salatblade med citrus mayonaise</li>
    <li>Cannelloni. Hjemmelavet pastarør fyldt med ricotta og spinat</li>
    <li>Førsteklasses helstegt oksemørbrad på en bund af grønne asparges, hertil små kartofler i koldpresset oliven­olie, slave af ovnstegt rodselleri og rødvinssauce</li>
  </ul>
  <ul class="course-list course-list--second">
    <li>Et udvalg af italienske oste med valnøddekerner</li>
    <li>Tiramisu, den italienske dessertklassiker med limoncello og skovbær</li>
  </ul>

  <p class="bread-note">Vores hjemmebagt brød med persillepesto får du selvfølgelig også med.</p>
  <p class="closing-line">Buon appetito!</p>
  <span class="corner-mark" aria-hidden="true"></span>
</section>

<section class="page page--everyday">
  <svg class="flag-corner" viewBox="0 0 84 84" aria-hidden="true">
    <polygon points="0,40 40,0 56,0 0,56" fill="var(--flag-green)"/>
    <polygon points="0,56 56,0 66,0 0,66" fill="#ffffff"/>
    <polygon points="0,66 66,0 84,0 0,84" fill="var(--flag-red)"/>
  </svg>

  <h2 class="everyday-title">MAD UD AF HUSET TIL HVERDAG<br>OG FEST PÅ ÆGTE ITALIENSK MANÉR</h2>
  <p class="everyday-intro">Uanset om det er tirsdag eller lørdag, og om man skal have mange gæster eller bare skal være alene hjemme, kan det være skønt med lidt hjælp til medlevningen. Trattoria Verde kan hjælpe dig med at sørge for maden, så du kun skal sørge for den hjemlige hygge. Vi her forskellige menuer man kan vælge mellem, men hvis man her specialønsker er man selvfølgelig velkommen til at ringe til restauranten og få en snak med vores søde personale.</p>

  <div class="menu-column menu-column--family">
    <p class="menu-column__intro">Familiepakker Middag til hele familien til en travl dag. Køb én pakke der indeholder nok til to børn og to voksne, der indeholder følgende:</p>
    <p>Familiepakke 1<br>2 x helstegt oksefilet, hertil små rosmarin kartofler, ovnstegte rodfrugter og valgfri sauce<br>2 x spaghetti bolognese<br>Pris kr 249,-</p>
    <p>Familiepakke 2<br>2 x grillet unghanebryst, hertil små kartofler i koldpresset olivenolie, grønne asparges og valgfri sauce<br>2 x lasagne<br>Pris kr 249,-</p>
  </div>

  <div class="menu-column menu-column--pairs">
    <p class="menu-column__intro">Pakker til min 2 personer Middag til to personer eller flere. Vælg mellem følgende:</p>
    <p>Pakke 1<br>Helstegt oksefilet, hertil små rosmarinkartofler, ovnstegte rodfrugter og valgfri sauce</p>
    <p>Pakke 2<br>Grillet unghanebryst, hertil små kartofler i koldpresset olivenolie, grønne asparges og valgfri sauce</p>
    <p>Pakke 3<br>Penne al filetto; Penne pasta med små stykker af oksemørbrad i fløde-svampe sauce</p>
    <p>Pakke 4<br>Penne al cinghiale; Penne med vildtragout af vildsvin og bacon med frisk revet parmesan</p>
    <p>Pris kun kr 175,- for to personer + 79 kr per ekstra kuvert</p>
  </div>

  <div class="menu-column menu-column--single">
    <p class="menu-column__intro">Bestil blot en enkelt ret eller flere. Kan også kombineres med pakkerne. Vælg mellem:</p>
    <p>Pakke 1<br>Helstegt oksefilet, hertil små rosmarinkartofler, ovnstegte rodfrugter og valgfri sauce</p>
    <p>Pakke 2<br>Grillet unghanebryst, hertil små kartofler i koldpresset olivenolie, grønne asparges og valgfri sauce</p>
    <p>Pakke 3<br>Penne al filetto; Penne pasta med små stykker af oksemørbrad i fløde-svampe sauce</p>
    <p>Pakke 4<br>Penne al cinghiale; Penne med vildtragout af vildsvin og bacon med frisk revet parmesan</p>
    <p>Pris kun kr 175,- for to personer + 79 kr per ekstra kuvert</p>
  </div>

  <p class="order-footer">Ønsker de at bestille andre retter fra vores a la carte kort, så ring til os<br>på telefon 86 40 12 57, udvalg og pris kan du se på trattoria-verde.dk</p>
</section>

</body>
</html>
```